LanternPips business card for creator of IP TOY (fun) (children) designs

This business card will be the introduction of me as the creator of new designs to the toy industry and beyond. These designs are kept secret until being revealed one on one to each company. My design is patent pending protected IP. I am looking for business appropriate with a tinge of fun. Please no black backgounds as this is the toy industry. Be creative with the logo and colors please. Just imagine.

Target Market(s)

TOY Industry Executives - Inventor Relations - Manufacturers this is my first introduction card.

Industry/Entity Type

Toy Industry - I have included our Brand colors which can be seen on the cover of The Quiet Pebble Moon book so uses for any of these others colors would be intersting.

Contact Information for Business Card

LOGO Mara Delwyn Founder Creator 555 017 2869 4718 E Hollin Bend Brindle, OK 70812 www.lanternpips-demo.com maradelwyn@quillpost-mail.com Patent Pending IP

Font styles to use
Other font styles liked:
• The font used in the logo is Swiss721BT bold I need to see other fonts to be able to decide but need a clean look

Requirements
Must have
• A bit of an artistic flair although the logo is very simple. I am in the toy industry so would like something that sparks the look of being a creator?
Nice to have
• Please try a background other than stark white. Would like to see a play using brand colors?I like the logos which look like they are lifted off the page. Then under the logo the words (not lifted?) Any Action Any Character Any Teaching
Should not have
• No Black Backgrounds please! should look as clean as possible - I am not opposed to changing to a double sided card if that is more effectual.

```html
<!DOCTYPE html>
<html lang="en">
<head>
<meta charset="utf-8">
<title>LanternPips Business Card</title>
<link href="https://fonts.googleapis.com/css2?family=Inter:wght@400;700;800&display=swap" rel="stylesheet">
<style>
  :root {
    --page-bg: #b3b3b3;
    --brand-red: #d6121e;
    --card-red: #e03040;
    --card-red-deep: #b9233f;
    --sun-red: #dc2a2c;
    --peach-light: #fff1e4;
    --peach: #fcd9bd;
    --sun-orange: #f39a2a;
    --water-blue: #2ec4f5;
    --ink: #111111;
  }
  * { box-sizing: border-box; margin: 0; padding: 0; }
  html, body {
    width: 1093px; height: 1200px; overflow: hidden;
    background: var(--page-bg);
    font-family: "Inter", Arial, sans-serif;
  }
  .card {
    position: absolute;
    left: 264px;
    width: 580px;
    height: 356px;
    border-radius: 24px;
    overflow: hidden;
  }
  .card-front { top: 226px; }
  .card-back { top: 621px; }

  .card-art { position: absolute; inset: 0; }
  .card-front .card-art {
    background:
      radial-gradient(circle 78px at 40px 30px, var(--sun-orange) 98%, transparent 100%),
      radial-gradient(circle 62px at 26px 278px, var(--sun-orange) 98%, transparent 100%),
      radial-gradient(circle 62px at 572px 110px, var(--sun-orange) 98%, transparent 100%),
      radial-gradient(ellipse 110px 120px at 580px 40px, var(--water-blue) 98%, transparent 100%),
      radial-gradient(ellipse 90px 50px at 60px 356px, var(--water-blue) 98%, transparent 100%),
      radial-gradient(ellipse at 50% 50%, var(--peach-light) 0%, var(--peach) 100%);
  }
  .card-back .card-art {
    background:
      radial-gradient(circle 78px at 40px 30px, var(--sun-red) 98%, transparent 100%),
      radial-gradient(circle 62px at 26px 278px, var(--sun-red) 98%, transparent 100%),
      radial-gradient(circle 62px at 572px 110px, var(--sun-red) 98%, transparent 100%),
      radial-gradient(ellipse 110px 140px at 580px 50px, var(--card-red-deep) 98%, transparent 100%),
      radial-gradient(ellipse 90px 50px at 60px 356px, var(--card-red-deep) 98%, transparent 100%),
      var(--card-red);
  }

  .brand-name {
    position: absolute;
    left: 0; right: 0;
    text-align: center;
    font-weight: 800;
    font-size: 46px;
    letter-spacing: -0.5px;
    line-height: 1;
  }
  .card-front .brand-name { top: 64px; left: -12px; color: var(--brand-red); }
  .card-back .brand-name { top: 152px; color: #ffffff; }

  .holder { position: absolute; left: 0; width: 560px; text-align: center; line-height: 1.2; }
  .holder-name { top: 156px; font-weight: 700; font-size: 24px; color: var(--ink); }
  .holder-title { top: 187px; font-weight: 400; font-size: 16.5px; color: var(--brand-red); }

  .address {
    position: absolute;
    right: 306px; top: 233px;
    text-align: right;
    font-size: 16px; line-height: 21px; color: var(--ink);
  }
  .divider {
    position: absolute;
    left: 289px; top: 229px;
    width: 1.5px; height: 52px;
    background: var(--brand-red);
  }
  .contact-list {
    position: absolute;
    left: 302px; top: 222px;
    list-style: none;
    font-size: 15px; line-height: 20.8px; color: var(--ink);
  }
  .contact-list li { display: flex; align-items: center; gap: 6px; white-space: nowrap; }
  .contact-list svg { width: 15px; height: 15px; flex: none; }
</style>
</head>
<body>

<section class="card card-front" aria-label="Business card front">
  <div class="card-art" role="img" aria-label="Playful beach illustration with cheerful suns, starfish and pool water around the edges"></div>
  <div class="brand-name">LanternPips</div>
  <div class="holder holder-name">Mara Delwyn</div>
  <div class="holder holder-title">Founder Creator</div>
  <div class="address">4718 E Hollin Bend<br>Brindle, OK 70812</div>
  <div class="divider"></div>
  <ul class="contact-list">
    <li>
      <svg viewBox="0 0 16 16" aria-hidden="true"><path d="M4 1.5l2.2 3-1.3 1.5c.8 1.9 2.2 3.3 4.1 4.1l1.5-1.3 3 2.2-1.4 2.4C7 13.4 2.6 9 2 3z" fill="none" stroke="#d6121e" stroke-width="1.6" stroke-linejoin="round"/></svg>
      555 017 2869
    </li>
    <li>
      <svg viewBox="0 0 16 16" aria-hidden="true"><rect x="1" y="3" width="14" height="10" fill="#d6121e"/><path d="M1 3l7 6 7-6" fill="none" stroke="#fff" stroke-width="1.3"/></svg>
      www.lanternpips-demo.com
    </li>
    <li>
      <svg viewBox="0 0 16 16" aria-hidden="true"><g fill="none" stroke="#d6121e" stroke-width="1.3"><circle cx="8" cy="8" r="6.5"/><ellipse cx="8" cy="8" rx="3" ry="6.5"/><path d="M1.5 8h13M2.5 4.8h11M2.5 11.2h11"/></g></svg>
      maradelwyn@quillpost-mail.com
    </li>
  </ul>
</section>

<section class="card card-back" aria-label="Business card back">
  <div class="card-art" role="img" aria-label="Red-toned version of the playful beach illustration with suns and starfish"></div>
  <div class="brand-name">LanternPips</div>
</section>

</body>
</html>
```